User Interface Designer Needed

I need a few designs for a property law comparison website. We assist the public with finding a solicitor for the purchase or sale of their house and units. We are currently in the process of creating a questionnaire based woo commerce product filter using gravity forms. I'd like to see designs that use the logo colours. Users will be selecting options such as "Buying" or "Selling", they will then be selecting options such as "House" "Unit" or "Land". Details attached. The final design should communicate ease and simplicity. Questions will be answered one at a time, and the next question is dependent on the answer to the question prior

Target Market(s)

First home buyers, people from ages 18-80 make and female looking to get rid of the hassle of ringing around and going from website to website trying to get a quote

Industry/Entity Type

Real Estate

Number of Pages Required

1 page

Colors
33a6d7

Requirements
Must have
• A design for every question
Nice to have
• Simple symbols or simplistic pictures incorporated, even better if you can turn the question into a picture instead of words eg. A picture of a house, a picture of a unit and a picture of land instead of written answers

```html
<!DOCTYPE html>
<html lang="en">
<head>
<meta charset="utf-8">
<title>Settlo.com.au – Property Solicitor Quotes</title>
<link rel="stylesheet" href="https://fonts.googleapis.com/css2?family=Open+Sans:wght@400;600;700;800&family=Raleway:wght@600;700;800&display=swap">
<style>
:root{
  --brand:#33a6d7;
  --brand-dark:#1f86b5;
  --navy:#1c2733;
  --navy-2:#243344;
  --footer:#1d4864;
  --footer-bar:#163a52;
  --ink:#2b2f33;
  --muted:#6d737a;
  --line:#d9dee3;
  --grey-bg:#eef0f2;
  --white:#ffffff;
}
*{box-sizing:border-box;margin:0;padding:0}
html,body{width:1200px;height:2868px;overflow:hidden}
body{font-family:"Open Sans",Arial,sans-serif;color:var(--ink);background:var(--white);position:relative;font-size:13px}
a{color:inherit;text-decoration:none}

/* header */
.site-header{height:96px;display:flex;align-items:center;justify-content:space-between;padding:0 80px}
.brand{display:flex;align-items:center;gap:10px;font-family:"Open Sans",sans-serif;font-weight:700;font-size:34px;color:var(--brand);white-space:nowrap}
.brand-dot{width:30px;height:30px;border-radius:50%;background:var(--brand);flex:0 0 auto}
.header-contact{display:flex;align-items:center;gap:24px;font-size:13px;color:var(--muted)}
.header-contact span{display:flex;align-items:center;gap:6px}
.btn-sm{background:var(--brand);color:#fff;padding:6px 14px;font-size:12px;font-weight:600}
.main-nav{height:40px;background:var(--navy);display:flex;justify-content:space-between;padding:0 80px}
.main-nav a{color:#fff;font-weight:700;font-size:13px;display:flex;align-items:center;padding:0 30px;letter-spacing:.5px}
.main-nav a.active{background:var(--navy-2);border-bottom:3px solid var(--brand)}
.main-nav a:last-child{padding-right:0}

/* hero */
.hero{position:relative;height:440px;background:linear-gradient(100deg,#3c4d5e 0%,#5f7283 45%,#2f3f50 100%)}
.hero-photo{position:absolute;inset:0}
.hero-title{position:absolute;left:80px;top:40px;color:#fff;font-family:"Raleway",sans-serif;font-weight:800;font-size:30px;line-height:1.2}
.hero-title::after{content:"";display:block;width:60px;height:3px;background:var(--brand);margin-top:12px}
.hero-arrow{position:absolute;top:200px;width:26px;height:40px;background:rgba(0,0,0,.5);display:flex;align-items:center;justify-content:center}
.hero-arrow.left{left:0}.hero-arrow.right{right:0}

/* search */
.search-panel{position:absolute;left:72px;top:530px;width:1056px}
.search-tabs{display:flex}
.search-tabs span{padding:10px 22px;font-weight:800;font-size:16px;display:flex;align-items:center;gap:8px}
.tab-buy{background:var(--white);color:var(--navy)}
.tab-sell{background:var(--brand);color:#fff}
.search-box{background:#fff;padding:22px 28px 24px;box-shadow:0 4px 14px rgba(0,0,0,.12)}
.field-grid{display:grid;grid-template-columns:repeat(3,1fr);gap:18px 40px}
.field label{display:block;font-size:12px;color:var(--ink);margin-bottom:6px}
.select{height:30px;border:1px solid var(--line);display:flex;align-items:center;justify-content:space-between;padding:0 0 0 10px;font-size:11px;color:var(--muted)}
.select i{width:28px;height:100%;border-left:1px solid var(--line);display:flex;align-items:center;justify-content:center}
.btn-search{display:block;margin:22px auto 0;width:150px;height:34px;background:var(--brand);color:#fff;font-weight:700;font-size:15px;text-align:center;line-height:34px;letter-spacing:1px}

/* headings */
.section-title{display:flex;align-items:center;justify-content:center;gap:16px;font-family:"Raleway",sans-serif;font-weight:800;font-size:36px;color:var(--navy)}
.section-title b{color:var(--brand);font-weight:800}
.section-title .rule{width:110px;height:1px;background:var(--line)}
.section-title .icon{width:34px;height:34px}

/* welcome */
.welcome{position:absolute;top:880px;left:0;width:1200px;text-align:center}
.welcome p{width:1040px;margin:22px auto 0;font-size:11.5px;line-height:1.65;color:var(--muted)}
.btn-outline{display:inline-block;margin-top:20px;background:var(--brand);color:#fff;padding:6px 16px;font-size:12px;font-weight:600}

/* featured */
.featured{position:absolute;top:1184px;left:0;width:1200px;height:536px;background:var(--brand)}
.featured .section-title{justify-content:flex-start;padding:28px 80px 0;color:#fff}
.featured .section-title b{color:var(--navy)}
.featured .underline{margin:6px 0 0 80px;width:1040px;height:1px;background:rgba(255,255,255,.5)}
.cards{display:grid;grid-template-columns:repeat(4,1fr);gap:14px;padding:22px 80px 0}
.card-photo{height:180px;border:4px solid #fff}
.card h3{color:#fff;font-size:18px;font-weight:700;margin-top:14px}
.card p{color:#eaf6fb;font-size:11.5px;line-height:1.55;margin-top:6px}
.card .more{color:#fff;font-size:11.5px;margin-top:8px;display:block}
.btn-dark{display:block;width:90px;margin:22px auto 0;background:#111;color:#fff;text-align:center;font-size:12px;padding:8px 0;font-weight:600}

/* testimonials */
.clients{position:absolute;top:1760px;left:0;width:1200px}
.quotes{display:grid;grid-template-columns:repeat(3,1fr);gap:30px;padding:46px 110px 0}
.quote{display:flex;gap:16px}
.avatar{flex:0 0 84px;height:84px;border-radius:50%;background:linear-gradient(#d9c6b2,#a88f78);border:3px solid #fff;box-shadow:0 0 0 1px var(--line)}
.quote p{font-size:11.5px;line-height:1.55;color:var(--muted)}
.quote .name{color:var(--brand);font-weight:700;font-size:11.5px;margin-top:8px}
.quote .name span{color:var(--muted);font-weight:400}
.pager{display:flex;justify-content:center;gap:10px;margin-top:34px}
.pager i{width:28px;height:28px;border-radius:50%;border:1px solid var(--brand);display:flex;align-items:center;justify-content:center}

/* news */
.news{position:absolute;top:2100px;left:0;width:1200px;height:460px;background:var(--grey-bg)}
.news .section-title{padding-top:34px}
.news-grid{position:relative;display:grid;grid-template-columns:1fr 1fr;gap:38px 110px;padding:40px 80px 0}
.news-grid::after{content:"";position:absolute;left:600px;top:40px;bottom:0;width:1px;background:var(--line)}
.news-item{display:flex;gap:16px}
.date{flex:0 0 50px;text-align:center}
.date .d{background:var(--brand);color:#fff;font-weight:800;font-size:22px;height:40px;line-height:40px}
.date .m{background:var(--navy);color:#fff;font-size:11px;height:22px;line-height:22px}
.news-item h4{font-size:17px;font-weight:600;color:var(--ink)}
.news-item p{font-size:11.5px;line-height:1.5;color:var(--muted);margin-top:6px}
.news .btn-outline{display:block;width:84px;margin:44px auto 0;text-align:center}

/* footer */
.site-footer{position:absolute;top:2580px;left:0;width:1200px;height:240px;background:var(--footer);color:#dfe9f0;display:grid;grid-template-columns:200px 260px 300px 1fr;padding:30px 80px 0}
.site-footer h5{font-size:15px;font-weight:700;color:#fff;margin-bottom:14px}
.site-footer h5 b{color:var(--brand);font-weight:400}
.links li{list-style:none;font-size:12px;line-height:24px;display:flex;gap:8px;align-items:center}
.links li::before{content:"";width:5px;height:5px;background:var(--brand)}
.contact-row{font-size:12px;line-height:1.5;display:flex;gap:8px;margin-bottom:10px}
.socials{display:flex;gap:8px;margin-top:6px}
.socials i{width:24px;height:24px;background:var(--brand)}
.news-form p{font-size:12px;margin-bottom:10px}
.input{height:28px;background:#fff;color:var(--muted);font-size:11px;padding:0 10px;line-height:28px;margin-bottom:8px;width:260px}
.btn-subscribe{width:260px;height:28px;background:var(--footer-bar);color:#fff;font-weight:700;font-size:12px;text-align:center;line-height:28px}
.footer-brand{display:flex;justify-content:flex-end;padding-top:70px;min-width:0}
.footer-brand .brand{color:#fff;font-size:28px;gap:8px}
.footer-brand .brand-dot{background:#fff;width:24px;height:24px}
.copyright{position:absolute;top:2820px;left:0;width:1200px;height:48px;background:var(--footer-bar);color:#c9d7e1;font-size:12px;text-align:center;line-height:48px}
</style>
</head>
<body>

<header class="site-header">
  <a class="brand" href="#"><span class="brand-dot"></span>Settlo.com.au</a>
  <div class="header-contact">
    <span><svg width="14" height="14" viewBox="0 0 14 14"><rect x="1" y="3" width="12" height="8" fill="none" stroke="#33a6d7" stroke-width="1.5"/><path d="M1 3l6 5 6-5" fill="none" stroke="#33a6d7" stroke-width="1.5"/></svg>info@settlo.com</span>
    <span><svg width="14" height="14" viewBox="0 0 14 14"><path d="M3 1l3 3-2 2c1 2 2 3 4 4l2-2 3 3-2 2C6 13 1 8 1 3z" fill="#33a6d7"/></svg>(555) 010 2030</span>
    <a class="btn-sm" href="#">Register</a>
    <a class="btn-sm" href="#">Log In</a>
  </div>
</header>

<nav class="main-nav">
  <a class="active" href="#">HOME</a>
  <a href="#">ABOUT US</a>
  <a href="#">FIXED FEES</a>
  <a href="#">ARTICLES</a>
  <a href="#">PROPERTY GALLERY</a>
  <a href="#">COMPANY</a>
  <a href="#">CONTACT US</a>
</nav>

<section class="hero">
  <div class="hero-photo" role="img" aria-label="Hand in a business suit holding a small model house"></div>
  <h1 class="hero-title">HELPING YOU MAKE THE<br>RIGHT MOVE</h1>
  <span class="hero-arrow left"><svg width="10" height="14"><path d="M8 1L2 7l6 6" stroke="#fff" stroke-width="2" fill="none"/></svg></span>
  <span class="hero-arrow right"><svg width="10" height="14"><path d="M2 1l6 6-6 6" stroke="#fff" stroke-width="2" fill="none"/></svg></span>
</section>

<form class="search-panel">
  <div class="search-tabs">
    <span class="tab-buy"><svg width="18" height="16"><path d="M1 2h3l2 9h9l2-7H5" fill="none" stroke="#33a6d7" stroke-width="2"/></svg>BUY</span>
    <span class="tab-sell"><svg width="16" height="16"><path d="M1 1h7l7 7-7 7-7-7z" fill="none" stroke="#fff" stroke-width="2"/></svg>SELL</span>
  </div>
  <div class="search-box">
    <div class="field-grid">
      <div class="field"><label>I am a</label><div class="select">Buyer<i><svg width="8" height="5"><path d="M0 0h8L4 5z" fill="#888"/></svg></i></div></div>
      <div class="field"><label>I am buying a</label><div class="select">House<i><svg width="8" height="5"><path d="M0 0h8L4 5z" fill="#888"/></svg></i></div></div>
      <div class="field"><label>I would like</label><div class="select">Select an option<i><svg width="8" height="5"><path d="M0 0h8L4 5z" fill="#888"/></svg></i></div></div>
      <div class="field"><label>I want my quote to include</label><div class="select">Select an option<i><svg width="8" height="5"><path d="M0 0h8L4 5z" fill="#888"/></svg></i></div></div>
      <div class="field"><label>Signed a contract</label><div class="select">Choose an option<i><svg width="8" height="5"><path d="M0 0h8L4 5z" fill="#888"/></svg></i></div></div>
      <div class="field"><label>Risk</label><div class="select">Select an option<i><svg width="8" height="5"><path d="M0 0h8L4 5z" fill="#888"/></svg></i></div></div>
    </div>
    <a class="btn-search" href="#">SEARCH</a>
  </div>
</form>

<section class="welcome">
  <h2 class="section-title"><span class="rule"></span><svg class="icon" viewBox="0 0 34 34"><path d="M4 17L17 5l13 12M8 14v15h18V14" fill="none" stroke="#1c2733" stroke-width="3"/></svg>WELCOME TO <b>SETTLO.COM.AU</b><span class="rule"></span></h2>
  <p>Lorem ipsum dolor sit amet, consectetur adipiscing elit, sed do eiusmod tempor incididunt ut labore et dolore magna aliqua. Ut enim ad minim veniam, quis nostrud exercitation ullamco laboris nisi ut aliquip ex ea commodo consequat. Duis aute irure dolor in reprehenderit in voluptate velit esse cillum dolore eu fugiat nulla pariatur. Excepteur sint occaecat cupidatat non proident, sunt in culpa qui officia deserunt mollit anim id est laborum. Sed ut perspiciatis unde omnis iste natus error sit voluptatem accusantium doloremque laudantium, totam rem aperiam eaque ipsa quae ab illo inventore veritatis.</p>
  <a class="btn-outline" href="#">Learn More</a>
</section>

<section class="featured">
  <h2 class="section-title"><svg class="icon" viewBox="0 0 34 34"><path d="M4 17L17 5l13 12M8 14v15h18V14" fill="none" stroke="#fff" stroke-width="3"/></svg>FEATURED <b>PROPERTY</b></h2>
  <div class="underline"></div>
  <div class="cards">
    <article class="card"><div class="card-photo" role="img" aria-label="White two storey family house" style="background:linear-gradient(#9fc3df,#d7dfe3 60%,#6f8f55)"></div><h3>Lorem Ipsum</h3><p>Lorem ipsum dolor sit amet, consectetur adipiscing elit sed do eiusmod tempor.</p><a class="more" href="#">More info »</a></article>
    <article class="card"><div class="card-photo" role="img" aria-label="Modern house with grey roof at dusk" style="background:linear-gradient(#5e7fa6,#8d8a84 60%,#4f6342)"></div><h3>Lorem Ipsum</h3><p>Lorem ipsum dolor sit amet, consectetur adipiscing elit sed do eiusmod tempor.</p><a class="more" href="#">More info »</a></article>
    <article class="card"><div class="card-photo" role="img" aria-label="Large brick house surrounded by trees" style="background:linear-gradient(#3f5a3a,#8a6a4c 60%,#4c6b37)"></div><h3>Lorem Ipsum</h3><p>Lorem ipsum dolor sit amet, consectetur adipiscing elit sed do eiusmod tempor.</p><a class="more" href="#">More info »</a></article>
    <article class="card"><div class="card-photo" role="img" aria-label="Stone family home with front lawn" style="background:linear-gradient(#8fb1d3,#b69a78 60%,#5d7a3e)"></div><h3>Lorem Ipsum</h3><p>Lorem ipsum dolor sit amet, consectetur adipiscing elit sed do eiusmod tempor.</p><a class="more" href="#">More info »</a></article>
  </div>
  <a class="btn-dark" href="#">View All</a>
</section>

<section class="clients">
  <h2 class="section-title"><span class="rule"></span><svg class="icon" viewBox="0 0 34 34"><rect x="3" y="6" width="18" height="13" rx="2" fill="#1c2733"/><rect x="13" y="13" width="18" height="13" rx="2" fill="#6d737a"/></svg>WHAT OUR <b>CLIENTS</b> HAS TO SAY<span class="rule"></span></h2>
  <div class="quotes">
    <div class="quote"><div class="avatar" role="img" aria-label="Customer portrait"></div><div><p>Lorem ipsum dolor consectetur adipiscing elit, sed do eiusmod tempor incididunt ut labore nulla facilisi.</p><div class="name">MIA CARTER, <span>Customer</span></div></div></div>
    <div class="quote"><div class="avatar" role="img" aria-label="Customer portrait"></div><div><p>Lorem ipsum dolor consectetur adipiscing elit, sed do eiusmod tempor incididunt ut labore nulla facilisi.</p><div class="name">LEO HART, <span>Customer</span></div></div></div>
    <div class="quote"><div class="avatar" role="img" aria-label="Customer portrait"></div><div><p>Lorem ipsum dolor consectetur adipiscing elit, sed do eiusmod tempor incididunt ut labore nulla facilisi.</p><div class="name">ANNA REED, <span>Customer</span></div></div></div>
  </div>
  <div class="pager">
    <i><svg width="8" height="10"><path d="M6 1L2 5l4 4" stroke="#33a6d7" stroke-width="2" fill="none"/></svg></i>
    <i><svg width="8" height="10"><path d="M2 1l4 4-4 4" stroke="#33a6d7" stroke-width="2" fill="none"/></svg></i>
  </div>
</section>

<section class="news">
  <h2 class="section-title"><span class="rule"></span><svg class="icon" viewBox="0 0 34 34"><rect x="4" y="6" width="26" height="22" fill="none" stroke="#1c2733" stroke-width="3"/><path d="M9 13h16M9 18h16M9 23h10" stroke="#1c2733" stroke-width="2"/></svg>LATEST <b>NEWS</b><span class="rule"></span></h2>
  <div class="news-grid">
    <article class="news-item"><div class="date"><div class="d">26</div><div class="m">Feb</div></div><div><h4>Lorem Ipsum Dolor</h4><p>Lorem ipsum dolor sit amet, sed diam nonummy nibh euismod tincidunt ut laoreet dolore magna aliquam erat volutpat [+]</p></div></article>
    <article class="news-item"><div class="date"><div class="d">26</div><div class="m">Feb</div></div><div><h4>Lorem Ipsum Dolor</h4><p>Lorem ipsum dolor sit amet, sed diam nonummy nibh euismod tincidunt ut laoreet dolore magna aliquam erat volutpat [+]</p></div></article>
    <article class="news-item"><div class="date"><div class="d">26</div><div class="m">Feb</div></div><div><h4>Lorem Ipsum Dolor</h4><p>Lorem ipsum dolor sit amet, sed diam nonummy nibh euismod tincidunt ut laoreet dolore magna aliquam erat volutpat [+]</p></div></article>
    <article class="news-item"><div class="date"><div class="d">26</div><div class="m">Feb</div></div><div><h4>Lorem Ipsum Dolor</h4><p>Lorem ipsum dolor sit amet, sed diam nonummy nibh euismod tincidunt ut laoreet dolore magna aliquam erat volutpat [+]</p></div></article>
  </div>
  <a class="btn-outline" href="#">View All</a>
</section>

<footer class="site-footer">
  <div>
    <h5>Quick <b>Links</b></h5>
    <ul class="links"><li>Home</li><li>About Us</li><li>Fixed Fees</li><li>Articles</li><li>Property Gallery</li><li>Contact Us</li></ul>
  </div>
  <div>
    <h5>Contact <b>Info</b></h5>
    <div class="contact-row"><svg width="12" height="16"><path d="M6 15C2 9 1 7 1 5a5 5 0 0110 0c0 2-1 4-5 10z" fill="#33a6d7"/></svg>Lorem ipsum dolor amet,<br>sed diam 2020</div>
    <div class="contact-row"><svg width="14" height="14"><path d="M3 1l3 3-2 2c1 2 2 3 4 4l2-2 3 3-2 2C6 13 1 8 1 3z" fill="#33a6d7"/></svg>(555) 010 2030</div>
    <div class="contact-row"><svg width="14" height="14"><rect x="1" y="3" width="12" height="8" fill="none" stroke="#33a6d7" stroke-width="1.5"/><path d="M1 3l6 5 6-5" fill="none" stroke="#33a6d7" stroke-width="1.5"/></svg>info@settlo.com</div>
    <h5 style="margin:12px 0 6px">Follow <b>Us</b></h5>
    <div class="socials"><i></i><i></i><i></i><i></i></div>
  </div>
  <div class="news-form">
    <h5>Newsletter <b>Signup</b></h5>
    <p>Enter your email address below.</p>
    <div class="input">Name</div>
    <div class="input">Email</div>
    <div class="btn-subscribe">SUBSCRIBE</div>
  </div>
  <div class="footer-brand"><span class="brand"><span class="brand-dot"></span>Settlo.com.au</span></div>
</footer>
<div class="copyright">© 2016 Settlo. All Rights Reserved.</div>

</body>
</html>
```